AN ELEGANT COSMETIC LABLE THAT CAN EASILY BE ALTERED TO FIT A VARIETY OF DIFFERENT PRODUCTS.

Predictable and ordinary designs are NOT welcome. Creative minds wanted.

Looking for a professional lable that is Canadian/USA Standard and compliant with the Personal Goods - Safety Statute in Onatrio. Which has a clean and elegant look, with a hint of holistic vibes.

This lable should be sleak and flexible to be altered to fit a variety of different products. Let your creativity come out with this project, the crazy and unpredictable are welcome.

This lable may be on the next biggest Cosmetic brand in the world. If you can see it, you can design it. All the best, looking forward to working with you.

Target Market(s)

Everyone who is looking for a clean natural lifestyle. The elite crowd.

Industry/Entity Type

Cosmetics

Font styles to use
Serif
Script

Colors

Designer to choose only greyscale colors for use in the design.

Requirements
Must have
• Company Name " VORELLI'S" and or Logo. See attachment
Nice to have
• One or more solid bars that can be colored to match the main product ingredient colour.
Should not have
• Too much different colors or images

```html
<!DOCTYPE html>
<html lang="en">
<head>
<meta charset="utf-8">
<title>Vorelli's – Dew Nectar Label Set</title>
<link href="https://fonts.googleapis.com/css2?family=Arimo:wght@400;700&family=Cormorant+Garamond:wght@500;600&family=Great+Vibes&display=swap" rel="stylesheet">
<style>
:root{
  --teal:#1fb5a5;
  --teal-deep:#0a6f62;
  --teal-soft:#a4e2d8;
  --ink:#111;
  --paper:#fff;
  --serif:"Cormorant Garamond",Georgia,serif;
  --sans:"Arimo",Arial,sans-serif;
  --script:"Great Vibes",cursive;
}
*{margin:0;padding:0;box-sizing:border-box}
html,body{width:1200px;height:623px;overflow:hidden;background:var(--paper)}
body{position:relative;font-family:var(--sans);color:var(--ink)}
.abs{position:absolute}

/* main jar label */
.band{left:95px;top:178px;width:680px;height:231px;background:linear-gradient(180deg,rgba(255,255,255,1) 0%,var(--teal-soft) 45%,var(--teal) 100%)}
.panel{background:var(--paper);border:2px solid var(--teal-deep);border-radius:5px}
.panel-left{left:114px;top:101px;width:176px;height:300px}
.panel-right{left:579px;top:101px;width:176px;height:300px}
.block{position:absolute;left:5px;right:5px;font-size:9.3px;line-height:10.6px;text-align:justify}
.block h4{font-size:9.8px;font-weight:700;line-height:11px}
.rule{position:absolute;left:2px;right:2px;height:1px;background:var(--teal-deep)}
.accent-bar{position:absolute;left:2px;right:2px;height:10px;background:var(--teal-deep)}

.icon-row{position:absolute;left:6px;right:6px;display:flex;justify-content:space-between;align-items:flex-start}
.icon-cell{display:flex;flex-direction:column;align-items:center;width:36px;position:relative}
.icon-cell+.icon-cell::before{content:"";position:absolute;left:-5px;top:2px;width:1px;height:16px;background:var(--teal-deep)}
.icon{width:17px;height:17px}
.icon-label{font-size:3.8px;color:var(--teal-deep);margin-top:2px;white-space:nowrap}

.brand{font-family:var(--sans);font-weight:400;color:var(--ink);text-align:center;letter-spacing:2px}
.tagline{font-family:var(--sans);font-size:4px;letter-spacing:3.2px;text-align:center}
.brand-square{border:2px solid var(--ink)}

.product-name{font-family:var(--serif);font-weight:500;line-height:.9}
.name-light{color:var(--paper)}
.name-deep{color:var(--teal-deep)}
.sub{font-family:var(--sans);letter-spacing:5px;color:var(--teal-deep);text-align:center}
.weight{font-family:var(--sans);color:var(--teal-deep);text-align:center}
.aloe-art{border-radius:40% 40% 8px 8px;background:linear-gradient(180deg,#3fa894,var(--teal-deep))}
.seal{border-radius:50%;border:2px solid var(--teal);background:radial-gradient(circle,var(--teal-deep) 0 45%,var(--paper) 47%)}

/* tube strip */
.strip{left:89px;top:436px;width:680px;height:98px;border:1px solid #666;background:linear-gradient(180deg,var(--paper) 20%,var(--teal-soft) 50%,var(--teal) 100%)}
.strip .panel{border-width:1.5px}
.mini{font-size:3.7px;line-height:4.4px;text-align:justify}
.mini h5{font-size:3.8px;font-weight:700}

/* round lid */
.lid{left:825px;top:193px;width:296px;height:296px;border-radius:50%;border:3px solid var(--teal);background:var(--paper)}
.script{font-family:var(--script);color:var(--ink)}
.url{font-family:var(--serif);font-weight:600;font-size:7px;letter-spacing:.5px;text-align:center}
</style>
</head>
<body>

<!-- MAIN JAR LABEL -->
<div class="abs band"></div>

<section class="abs panel panel-left">
  <div class="block" style="top:14px">
    <h4>INGREDIENTS:</h4>
    Aloe Gel, Coconut Oil, Water, Cetearyl Alcohol, Glycerin, Sunflower Oil, Shea Butter, Glycerin Stearate, Beeswax, Dimethicon, Phenoxyethanol, Vitamin E, Sodium Polyacrylate.
  </div>
  <div class="rule" style="top:82px"></div>
  <div class="block" style="top:88px">
    <h4>INGRÉDIENTS:</h4>
    Gel d’aloès, huile de noix de coco, eau, alcool cetearyl, glycérine, huile de tournesol, beurre de karité, stéarate de glycérine, cire d’abeille, diméthicone, phénoxyéthanol, vitamine E, polyacrylate de sodium.
  </div>
  <div class="accent-bar" style="top:168px"></div>
  <div class="block" style="top:186px">
    <h4>WARNING:</h4>
    This product is not intended for human consumption. If irritation occurs, discontinue use.
  </div>
  <div class="rule" style="top:232px"></div>
  <div class="block" style="top:239px">
    <h4>ATTENTION:</h4>
    Ce produit n’est pas destiné à la consommation humaine. En cas d’irritation, cesser l’utilisation.
  </div>
</section>

<div class="abs brand-square" style="left:420px;top:103px;width:30px;height:30px"></div>
<div class="abs brand" style="left:370px;top:137px;width:130px;font-size:13px">VORELLI'S</div>
<div class="abs tagline" style="left:370px;top:148px;width:130px">MADE FOR YOU</div>

<div class="abs aloe-art" role="img" aria-label="Aloe vera plant illustration" style="left:392px;top:190px;width:75px;height:75px"></div>
<div class="abs seal" role="img" aria-label="Natural ingredients seal" style="left:470px;top:182px;width:40px;height:40px"></div>
<div class="abs" style="left:380px;top:268px;width:98px;text-align:center;font-size:6.5px;letter-spacing:1.3px;color:var(--paper)">ALOE VERA</div>

<div class="abs product-name name-light" style="left:358px;top:288px;font-size:34px">Dew</div>
<div class="abs product-name name-deep" style="left:358px;top:318px;font-size:40px">Nectar</div>
<div class="abs sub" style="left:335px;top:365px;width:190px;font-size:9.5px">PEAU NECTAR</div>
<div class="abs weight" style="left:370px;top:390px;width:120px;font-size:6px">453.59 g / 16 oz</div>

<section class="abs panel panel-right">
  <div class="block" style="top:10px">
    <h4>DETAILS:</h4>
    Luxuriously rich moisturizer that melts effortlessly into the skin, leaving it soft and luminous. This formulation is pH-optimized for glowing skin that remains hydrated and protected all day long. It leaves no sticky residues and is easy to spread while still maintaining the look and feel of a premium product.
  </div>
  <div class="icon-row" style="top:111px">
    <div class="icon-cell"><svg class="icon" viewBox="0 0 20 20"><circle cx="10" cy="10" r="8.5" fill="none" stroke="#0a6f62" stroke-width="1.5"/><line x1="4" y1="16" x2="16" y2="4" stroke="#0a6f62" stroke-width="1.3"/></svg><span class="icon-label">Gluten FREE</span></div>
    <div class="icon-cell"><svg class="icon" viewBox="0 0 20 20"><circle cx="10" cy="10" r="8.5" fill="none" stroke="#0a6f62" stroke-width="1.5"/><line x1="4" y1="16" x2="16" y2="4" stroke="#0a6f62" stroke-width="1.3"/></svg><span class="icon-label">Phthalate FREE</span></div>
    <div class="icon-cell"><svg class="icon" viewBox="0 0 20 20"><circle cx="10" cy="10" r="8.5" fill="none" stroke="#0a6f62" stroke-width="1.5"/><line x1="4" y1="16" x2="16" y2="4" stroke="#0a6f62" stroke-width="1.3"/></svg><span class="icon-label">Fragrance FREE</span></div>
    <div class="icon-cell"><svg class="icon" viewBox="0 0 20 20"><circle cx="10" cy="10" r="8.5" fill="none" stroke="#0a6f62" stroke-width="1.5"/><line x1="4" y1="16" x2="16" y2="4" stroke="#0a6f62" stroke-width="1.3"/></svg><span class="icon-label">Cruelty FREE</span></div>
  </div>
  <div class="block" style="top:143px">
    <h4>DÉTAILS:</h4>
    Crème hydratante luxueusement riche qui fond sans effort dans la peau, la laissant douce et lumineuse. Cette formulation est optimisée pour le pH pour une peau éclatante qui reste hydratée et protégée toute la journée. Il ne laisse pas de résidus collants et est facile à étaler tout en conservant l'apparence et la convivialité d'un produit haut de gamme.
  </div>
  <div class="icon-row" style="top:264px">
    <div class="icon-cell"><svg class="icon" viewBox="0 0 20 20"><circle cx="10" cy="10" r="8.5" fill="none" stroke="#0a6f62" stroke-width="1.5"/><line x1="4" y1="16" x2="16" y2="4" stroke="#0a6f62" stroke-width="1.3"/></svg><span class="icon-label">Sans gluten</span></div>
    <div class="icon-cell"><svg class="icon" viewBox="0 0 20 20"><circle cx="10" cy="10" r="8.5" fill="none" stroke="#0a6f62" stroke-width="1.5"/><line x1="4" y1="16" x2="16" y2="4" stroke="#0a6f62" stroke-width="1.3"/></svg><span class="icon-label">Phtalate GRATUIT</span></div>
    <div class="icon-cell"><svg class="icon" viewBox="0 0 20 20"><circle cx="10" cy="10" r="8.5" fill="none" stroke="#0a6f62" stroke-width="1.5"/><line x1="4" y1="16" x2="16" y2="4" stroke="#0a6f62" stroke-width="1.3"/></svg><span class="icon-label">Sans parfum</span></div>
    <div class="icon-cell"><svg class="icon" viewBox="0 0 20 20"><circle cx="10" cy="10" r="8.5" fill="none" stroke="#0a6f62" stroke-width="1.5"/><line x1="4" y1="16" x2="16" y2="4" stroke="#0a6f62" stroke-width="1.3"/></svg><span class="icon-label">Cruauté GRATUITE</span></div>
  </div>
</section>

<!-- TUBE STRIP -->
<div class="abs strip">
  <section class="abs panel mini" style="left:7px;top:7px;width:200px;height:82px;padding:4px">
    <h5>INGREDIENTS:</h5>
    <p>Aloe Gel, Coconut Oil, Water, Cetearyl Alcohol, Glycerin, Sunflower Oil, Shea Butter, Glycerin Stearate, Beeswax, Dimethicon, Phenoxyethanol, Vitamin E, Sodium Polyacrylate.</p>
    <h5 style="margin-top:3px">INGRÉDIENTS:</h5>
    <p>Gel d’aloès, huile de noix de coco, eau, alcool cetearyl, glycérine, huile de tournesol, beurre de karité, stéarate de glycérine, cire d’abeille, diméthicone, phénoxyéthanol, vitamine E, polyacrylate de sodium.</p>
    <div style="height:5px;background:var(--teal-deep);margin:6px 0 7px"></div>
    <h5>WARNING:</h5>
    <p>This product is not intended for human consumption. If irritation occurs, discontinue use.</p>
    <div style="height:.5px;background:var(--teal-deep);margin:2px 0"></div>
    <h5>ATTENTION:</h5>
    <p>Ce produit n’est pas destiné à la consommation humaine. En cas d’irritation, cesser l’utilisation.</p>
  </section>

  <div class="abs brand-square" style="left:282px;top:8px;width:13px;height:13px;border-width:1px"></div>
  <div class="abs brand" style="left:298px;top:7px;font-size:11px">VORELLI'S</div>
  <div class="abs tagline" style="left:300px;top:18px;width:76px;font-size:3px;letter-spacing:2px">MADE FOR YOU</div>
  <div class="abs aloe-art" role="img" aria-label="Aloe vera plant illustration" style="left:235px;top:33px;width:37px;height:40px"></div>
  <div class="abs" style="left:230px;top:75px;width:48px;text-align:center;font-size:3.5px;color:var(--paper)">ALOE VERA</div>
  <div class="abs product-name" style="left:278px;top:32px;font-size:21px;white-space:nowrap"><span class="name-light">Dew</span> <span class="name-deep">Nectar</span></div>
  <div class="abs sub" style="left:290px;top:61px;width:100px;font-size:5.5px;letter-spacing:2.6px">PEAU NECTAR</div>
  <div class="abs weight" style="left:300px;top:81px;width:80px;font-size:5px">226.8 g / 8 oz</div>
  <div class="abs seal" role="img" aria-label="Natural ingredients seal" style="left:413px;top:39px;width:30px;height:30px;border-width:1.5px"></div>

  <section class="abs panel mini" style="left:474px;top:7px;width:200px;height:82px;padding:4px">
    <div style="display:flex;gap:5px">
      <div style="flex:1;padding-right:3px;border-right:.5px solid var(--teal-deep);height:56px">
        <h5>DETAILS:</h5>
        <p>Luxuriously rich moisturizer that melts effortlessly into the skin, leaving it soft and luminous. This formulation is pH-optimized for glowing skin that remains hydrated and protected all day long. It leaves no sticky residues and is easy to spread while still maintaining the look and feel of a premium product.</p>
      </div>
      <div style="flex:1">
        <h5>DÉTAILS:</h5>
        <p>Crème hydratante luxueusement riche qui fond sans effort dans la peau, la laissant douce et lumineuse. Cette formulation est optimisée pour le pH pour une peau éclatante qui reste hydratée et protégée toute la journée. Il ne laisse pas de résidus collants et est facile à étaler tout en conservant l'apparence et la convivialité d'un produit haut de gamme.</p>
      </div>
    </div>
    <div style="display:flex;justify-content:space-between;margin-top:4px">
      <svg width="11" height="11" viewBox="0 0 20 20"><circle cx="10" cy="10" r="8.5" fill="none" stroke="#0a6f62" stroke-width="1.8"/><line x1="4" y1="16" x2="16" y2="4" stroke="#0a6f62" stroke-width="1.5"/></svg>
      <svg width="11" height="11" viewBox="0 0 20 20"><circle cx="10" cy="10" r="8.5" fill="none" stroke="#0a6f62" stroke-width="1.8"/><line x1="4" y1="16" x2="16" y2="4" stroke="#0a6f62" stroke-width="1.5"/></svg>
      <svg width="11" height="11" viewBox="0 0 20 20"><circle cx="10" cy="10" r="8.5" fill="none" stroke="#0a6f62" stroke-width="1.8"/><line x1="4" y1="16" x2="16" y2="4" stroke="#0a6f62" stroke-width="1.5"/></svg>
      <svg width="11" height="11" viewBox="0 0 20 20"><circle cx="10" cy="10" r="8.5" fill="none" stroke="#0a6f62" stroke-width="1.8"/><line x1="4" y1="16" x2="16" y2="4" stroke="#0a6f62" stroke-width="1.5"/></svg>
      <svg width="11" height="11" viewBox="0 0 20 20"><circle cx="10" cy="10" r="8.5" fill="none" stroke="#0a6f62" stroke-width="1.8"/><line x1="4" y1="16" x2="16" y2="4" stroke="#0a6f62" stroke-width="1.5"/></svg>
      <svg width="11" height="11" viewBox="0 0 20 20"><circle cx="10" cy="10" r="8.5" fill="none" stroke="#0a6f62" stroke-width="1.8"/><line x1="4" y1="16" x2="16" y2="4" stroke="#0a6f62" stroke-width="1.5"/></svg>
      <svg width="11" height="11" viewBox="0 0 20 20"><circle cx="10" cy="10" r="8.5" fill="none" stroke="#0a6f62" stroke-width="1.8"/><line x1="4" y1="16" x2="16" y2="4" stroke="#0a6f62" stroke-width="1.5"/></svg>
      <svg width="11" height="11" viewBox="0 0 20 20"><circle cx="10" cy="10" r="8.5" fill="none" stroke="#0a6f62" stroke-width="1.8"/><line x1="4" y1="16" x2="16" y2="4" stroke="#0a6f62" stroke-width="1.5"/></svg>
    </div>
  </section>
</div>

<!-- ROUND LID -->
<div class="abs lid"></div>
<div class="abs product-name" style="left:906px;top:224px;font-size:33px;color:var(--teal)">Dew</div>
<div class="abs product-name name-deep" style="left:906px;top:252px;font-size:38px">Nectar</div>
<div class="abs brand-square" style="left:946px;top:298px;width:54px;height:54px;border-width:3px"></div>
<div class="abs brand" style="left:883px;top:358px;width:180px;font-size:19px;letter-spacing:3px">VORELLI'S</div>
<div class="abs tagline" style="left:883px;top:377px;width:180px;font-size:6px;letter-spacing:5px;font-weight:700">MADE FOR YOU</div>
<div class="abs product-name" style="left:873px;top:396px;width:200px;text-align:center;font-size:19px;color:var(--teal)">Peau Nectar</div>
<div class="abs script" style="left:873px;top:414px;width:200px;text-align:center;font-size:24px">Faite pour vous</div>
<div class="abs url" style="left:873px;top:455px;width:200px">WWW.VORELLIS.COM</div>

</body>
</html>
```